Home Remodeling company needs a business card design

we need a business card design for home remodeling company in hamilton county, indiana USA. we offers a wide range of construction services including whole house renovations, Design and Build Basements and Kitchen and Bathroom Remodeling . we would like to see designs for both site of business card that use the same color of the company logo and also including all information below :
1- Tarek Salim CEO / General Contractor
2- all company contacts Telephone numbers ( 1-888-VOLMI-15 ) ( 317-555-0192) email address ( info@volmihome.example) website ( www.volmihome.example ) and social media logos (Facebook- twitter- google plus )
3- company logo
4- licensed . insured . bonded

```html
<!DOCTYPE html>
<html lang="en">
<head>
<meta charset="utf-8">
<title>Volmi Business Card</title>
<link rel="stylesheet" href="https://fonts.googleapis.com/css2?family=Open+Sans:wght@400;700;800&display=swap">
<style>
  :root {
    --backdrop: #2b2b2b;
    --card: #f1f4f8;
    --brand-red: #d0343c;
    --ink: #3a3a3c;
    --ink-soft: #555558;
  }
  * { margin: 0; padding: 0; box-sizing: border-box; }
  html, body { width: 1200px; height: 879px; overflow: hidden; }
  body {
    background: var(--backdrop);
    font-family: "Open Sans", Arial, sans-serif;
    position: relative;
  }
  .card {
    position: absolute;
    width: 620px;
    height: 354px;
    background: var(--card);
    overflow: hidden;
    box-shadow: 0 10px 30px rgba(0,0,0,0.5);
  }
  .card-front { left: 70px; top: 70px; }
  .card-back { left: 510px; top: 455px; }
  .swoosh { position: absolute; left: 0; top: 0; width: 620px; height: 354px; }
  .wordmark {
    position: absolute;
    display: flex;
    align-items: center;
    gap: 10px;
    font-weight: 800;
    color: var(--ink);
    letter-spacing: 1px;
    line-height: 1;
  }
  .wordmark-mark {
    width: 12px; height: 12px;
    background: var(--brand-red);
  }
  .card-front .wordmark { left: 150px; top: 135px; font-size: 52px; }
  .card-back .wordmark { left: 40px; top: 88px; font-size: 42px; }
  .holder {
    position: absolute;
    right: 40px;
    top: 40px;
    text-align: right;
  }
  .holder-name { font-size: 23px; font-weight: 700; color: var(--ink); }
  .holder-title { font-size: 14px; color: var(--ink-soft); margin-top: 6px; }
  .contacts {
    position: absolute;
    right: 28px;
    top: 132px;
    list-style: none;
  }
  .contact {
    display: flex;
    justify-content: flex-end;
    align-items: center;
    gap: 12px;
    font-size: 16px;
    color: var(--ink);
    height: 22px;
  }
  .contact svg { width: 12px; height: 12px; fill: var(--brand-red); flex: none; }
</style>
</head>
<body>

<section class="card card-front" aria-label="Card front">
  <svg class="swoosh" viewBox="0 0 620 354" aria-hidden="true">
    <path d="M0 354 L0 318 C200 300 420 240 620 130 L620 354 Z" fill="var(--brand-red)"/>
    <path d="M0 330 C220 312 430 250 620 150 L620 160 C430 262 220 322 0 340 Z" fill="var(--card)"/>
    <path d="M0 345 C230 326 440 262 620 168 L620 176 C440 272 230 334 0 352 Z" fill="var(--ink)"/>
    <path d="M260 262 C400 235 520 190 620 120 L620 126 C520 198 400 242 260 262 Z" fill="var(--brand-red)"/>
  </svg>
  <div class="wordmark"><span class="wordmark-mark"></span>VOLMI</div>
</section>

<section class="card card-back" aria-label="Card back">
  <svg class="swoosh" viewBox="0 0 620 354" aria-hidden="true">
    <path d="M0 354 L0 310 C200 300 420 285 620 255 L620 354 Z" fill="var(--brand-red)"/>
    <path d="M0 320 C210 310 430 294 620 264 L620 272 C430 302 210 318 0 328 Z" fill="var(--card)"/>
    <path d="M0 334 C220 324 440 306 620 278 L620 288 C440 316 220 332 0 342 Z" fill="var(--ink)"/>
    <path d="M260 290 C400 278 520 262 620 238 L620 244 C520 268 400 282 260 290 Z" fill="var(--brand-red)"/>
  </svg>

  <div class="wordmark"><span class="wordmark-mark"></span>VOLMI</div>

  <div class="holder">
    <p class="holder-name">Tarek Salim</p>
    <p class="holder-title">CEO /GC</p>
  </div>

  <ul class="contacts">
    <li class="contact">317-555-0192
      <svg viewBox="0 0 12 12" aria-hidden="true"><path d="M3 0h6a1 1 0 0 1 1 1v10a1 1 0 0 1-1 1H3a1 1 0 0 1-1-1V1a1 1 0 0 1 1-1zm0 1.5v8h6v-8z"/></svg>
    </li>
    <li class="contact">1-888-VOLMI-15
      <svg viewBox="0 0 12 12" aria-hidden="true"><path d="M0 4c0-2 3-3 6-3s6 1 6 3v1H9V3.5H3V5H0zM2 6h8l1 5H1z"/></svg>
    </li>
    <li class="contact">info@volmihome.example
      <svg viewBox="0 0 12 12" aria-hidden="true"><path d="M0 2h12v8H0zm1 1 5 4 5-4z"/></svg>
    </li>
    <li class="contact">www.volmihome.example
      <svg viewBox="0 0 12 12" aria-hidden="true"><path d="M6 0a6 6 0 1 1 0 12A6 6 0 0 1 6 0zm0 1.5a4.5 4.5 0 1 0 0 9 4.5 4.5 0 0 0 0-9zM1.5 5.5h9v1h-9zM5.5 1.5h1v9h-1z"/></svg>
    </li>
  </ul>
</section>

</body>
</html>
```